Medical Company in need of a Modern Flyer design for new Wound Care clinic.

Tri-Fold modern flyer design for our Woundcare company. Logo and description of services can be found on our website; https://www.corvin-woundcare.com/

```html
<!DOCTYPE html>
<html lang="en">
<head>
<meta charset="utf-8">
<title>Corvin Woundcare – Tri-Fold Brochure</title>
<link href="https://fonts.googleapis.com/css2?family=Great+Vibes&family=Poppins:wght@400;500;600;700&display=swap" rel="stylesheet">
<style>
  :root{
    --page:#ecebe8;
    --gold:#b98c4e;
    --gold-dark:#a17536;
    --gold-light:#c9a46b;
    --ink:#1f1f1f;
    --charcoal:#262626;
    --white:#ffffff;
    --muted:#f2efe9;
  }
  *{box-sizing:border-box;margin:0;padding:0}
  html,body{width:804px;height:1200px;overflow:hidden}
  body{background:var(--page);font-family:"Poppins",sans-serif;color:var(--ink);position:relative}

  .brochure{
    position:absolute;left:22px;top:355px;width:760px;height:490px;
    display:grid;grid-template-columns:253px 254px 253px;
    box-shadow:0 10px 30px rgba(0,0,0,.18);background:var(--white);
  }
  .panel{position:relative;display:flex;flex-direction:column;overflow:hidden}
  .panel__body{flex:1;position:relative}
  .panel__footer{
    height:30px;background:var(--white);display:flex;align-items:center;justify-content:center;
    font-size:9.5px;font-weight:600;color:var(--ink);letter-spacing:.1px;
  }

  /* brand name */
  .brand{display:flex;align-items:center;justify-content:center;gap:6px;
    font-size:12.5px;font-weight:500;letter-spacing:1.4px;color:var(--ink)}
  .brand__dot{width:9px;height:9px;border-radius:50%;background:var(--gold)}

  /* left panel */
  .panel--intro .panel__body{background:linear-gradient(160deg,var(--gold-light) 0%,var(--gold) 45%,var(--gold-dark) 100%);padding:26px 22px 0 26px;color:var(--white)}
  .headline__script{font-family:"Great Vibes",cursive;font-size:52px;line-height:.9;display:inline-block}
  .headline__small{font-size:14px;font-weight:500;margin-left:2px}
  .headline__bold{font-size:23px;font-weight:700;line-height:1.15;margin-top:2px}
  .features{list-style:none;margin-top:36px;display:flex;flex-direction:column;gap:22px}
  .feature{display:flex;gap:10px;align-items:flex-start}
  .feature__icon{flex:0 0 34px;height:34px;border-radius:50%;background:var(--white);display:flex;align-items:center;justify-content:center;margin-top:2px}
  .feature__title{font-size:9px;font-weight:600;margin-bottom:3px}
  .feature__text{font-size:6.6px;line-height:1.45;opacity:.95}

  /* middle panel */
  .panel--contact .panel__body{background:linear-gradient(180deg,#1f1f1f 0%,#2c2c2c 100%)}
  .contact-photo{position:absolute;left:0;right:0;top:0;height:230px;
    background:linear-gradient(180deg,#f7f7f5 0%,#e4e8ea 28%,#c9d0d1 52%,#8d918f 78%,#2a2a2a 100%)}
  .panel--contact .brand{position:absolute;top:30px;left:0;right:0}
  .contact{position:absolute;top:248px;left:0;right:0;text-align:center;color:var(--white)}
  .contact__title{font-size:10.5px;font-weight:500;margin-bottom:14px}
  .contact__icon{width:24px;height:24px;border-radius:50%;background:var(--gold);margin:0 auto 8px;display:flex;align-items:center;justify-content:center}
  .contact__line{font-size:9.5px;margin-bottom:22px}

  /* right panel */
  .panel--cover .panel__body{background:var(--white)}
  .panel--cover .brand{position:absolute;top:30px;left:0;right:0}
  .cover-photo{position:absolute;top:62px;left:0;right:0;height:160px;
    background:linear-gradient(180deg,#eef0ec 0%,#d9ddd4 45%,#c4c7be 100%)}
  .cover-band{position:absolute;top:232px;left:0;right:0;bottom:0;
    background:linear-gradient(160deg,var(--gold-light) 0%,var(--gold) 50%,var(--gold-dark) 100%)}
  .inset-photos{position:absolute;top:192px;left:10px;display:flex;gap:4px}
  .inset-photo{width:74px;height:62px;border:3px solid var(--white);background:linear-gradient(160deg,#d8dde2,#9aa4ad)}
  .inset-photo--two{background:linear-gradient(160deg,#c9d1dc,#6d7a8a)}
  .cover-title{position:absolute;top:285px;left:0;right:0;text-align:center;color:var(--white)}
  .cover-title__main{font-size:16px;font-weight:600;line-height:1.2}
  .cover-title__sub{font-size:9px;margin-top:8px;line-height:1.35}
</style>
</head>
<body>
<main class="brochure">

  <section class="panel panel--intro">
    <div class="panel__body">
      <h1 class="headline">
        <span class="headline__script">Caring</span>
        <span class="headline__small">for Your</span>
        <span class="headline__bold" style="display:block">Well-being</span>
      </h1>
      <ul class="features">
        <li class="feature">
          <span class="feature__icon">
            <svg width="18" height="18" viewBox="0 0 24 24" fill="none" stroke="#b98c4e" stroke-width="1.8" stroke-linejoin="round"><path d="M3 5h12v8H8l-3 3v-3H3z"/><path d="M17 9h4v8h-2v3l-3-3h-5v-2"/></svg>
          </span>
          <div>
            <h2 class="feature__title">Accepted Health Plans</h2>
            <p class="feature__text">We accept most major insurance plans to make your care as accessible and affordable as possible!</p>
          </div>
        </li>
        <li class="feature">
          <span class="feature__icon">
            <svg width="18" height="18" viewBox="0 0 24 24" fill="none" stroke="#b98c4e" stroke-width="1.8"><circle cx="12" cy="7" r="3"/><circle cx="5" cy="10" r="2.2"/><circle cx="19" cy="10" r="2.2"/><path d="M7 20c0-3 2.2-5 5-5s5 2 5 5"/><path d="M1.5 19c0-2.3 1.5-4 3.5-4M22.5 19c0-2.3-1.5-4-3.5-4"/></svg>
          </span>
          <div>
            <h2 class="feature__title">Expert Medical Team</h2>
            <p class="feature__text">Comprised of highly trained physicians, nurses, and specialists, our team brings years of experience in treating a wide range of complex wounds. With a commitment to innovative treatments and personalized care plans, we work closely with each patient to ensure optimal healing and recovery. Trust our team to provide the expert care you need for lasting results.</p>
          </div>
        </li>
        <li class="feature">
          <span class="feature__icon">
            <svg width="18" height="18" viewBox="0 0 24 24" fill="none" stroke="#b98c4e" stroke-width="1.8" stroke-linejoin="round"><path d="M12 21s-8-4.8-8-10.5A4.5 4.5 0 0 1 12 8a4.5 4.5 0 0 1 8 2.5C20 16.2 12 21 12 21z"/><path d="M9 13l2 2 4-4"/></svg>
          </span>
          <div>
            <h2 class="feature__title">Trusted Healthcare Provider</h2>
            <p class="feature__text">We specialize in advanced treatment modalities, using a multi-faceted approach to heal your patient's wound.</p>
          </div>
        </li>
      </ul>
    </div>
    <footer class="panel__footer">www.corvin-woundcare.com</footer>
  </section>

  <section class="panel panel--contact">
    <div class="panel__body">
      <div class="contact-photo" role="img" aria-label="Bright clinic waiting lounge with sofa, plants and large windows"></div>
      <div class="brand"><span class="brand__dot"></span>CORVIN WOUNDCARE</div>
      <div class="contact">
        <h2 class="contact__title">Get In Touch</h2>
        <div class="contact__icon">
          <svg width="12" height="12" viewBox="0 0 24 24" fill="none" stroke="#fff" stroke-width="2.2"><path d="M12 22s7-7 7-12a7 7 0 0 0-14 0c0 5 7 12 7 12z"/><circle cx="12" cy="10" r="2.5"/></svg>
        </div>
        <p class="contact__line">4120 Meadow Ridge Dr., Suite 12</p>
        <div class="contact__icon">
          <svg width="12" height="12" viewBox="0 0 24 24" fill="none" stroke="#fff" stroke-width="2.2"><rect x="7" y="2" width="10" height="20" rx="2"/><path d="M11 18h2"/></svg>
        </div>
        <p class="contact__line">555-014-2290</p>
      </div>
    </div>
    <footer class="panel__footer">www.corvin-woundcare.com</footer>
  </section>

  <section class="panel panel--cover">
    <div class="panel__body">
      <div class="brand"><span class="brand__dot"></span>CORVIN WOUNDCARE</div>
      <div class="cover-photo" role="img" aria-label="Hyperbaric oxygen therapy chamber with open hatch in a treatment room"></div>
      <div class="cover-band"></div>
      <div class="inset-photos">
        <div class="inset-photo" role="img" aria-label="Clinician smiling beside a chamber"></div>
        <div class="inset-photo inset-photo--two" role="img" aria-label="Patient wearing an oxygen hood during therapy"></div>
      </div>
      <div class="cover-title">
        <h2 class="cover-title__main">Hyperbaric<br>Oxygen Therapy</h2>
        <p class="cover-title__sub">A Cornerstone of Advanced<br>Wound Care</p>
      </div>
    </div>
    <footer class="panel__footer">www.corvin-woundcare.com</footer>
  </section>

</main>
</body>
</html>
```